Werbebanner Set für einen Matratzen Onlineshop
Zielgruppe
Unser Onlineshop vertreibt hochwertige und qualitative Matratzen über das Internet. Unsere Zielgruppe sind Kunden die nicht auf einer Rollmatratze schlafen wollen, sondern auch bereit sind ab 200 Euro für eine Matratze zu bezahlen.
Aufgabenstellung
Bitte erstellen Sie uns Werbebanner für unser Affiliate und Retagrgeting Programm in folgenden Größen:
250 x 250
200 x 200
468 x 60
728 x 90
300 x 250
120 x 600
160 x 600
Bitte lehnen Sie das Design an unseren Onlineshop an.
Unser Slogan:
weil Ihr Schlaf den Tag bestimmt
Wichtige Punkte die Signalisiert werden sollten:
Versandkostenfreier Versand!
Blauer Anker geprüft!
100 Tage Probe Schlafen!
Sollten Sie noch Grafiken oder Bilder benötigen, dürfen Sie sich gerne auf unserer Webseite bedienen.

```html
<!DOCTYPE html>
<html lang="de">
<head>
<meta charset="utf-8">
<title>Schlummerhaus Werbebanner</title>
<link href="https://fonts.googleapis.com/css2?family=Roboto+Condensed:wght@400;700&display=swap" rel="stylesheet">
<style>
  :root {
    --blue-dark: #0a63b8;
    --blue-mid: #1c7fd6;
    --blue-light: #4aa3ea;
    --logo-blue: #a9cdee;
    --green: #6aa84f;
    --green-text: #5e9e3e;
    --white: #ffffff;
    --frame: #d6d6d6;
    --mattress-light: #f4f5f6;
    --mattress-shade: #c9cdd2;
  }
  * { margin: 0; padding: 0; box-sizing: border-box; }
  html, body { width: 1200px; height: 1156px; overflow: hidden; background: var(--white); }
  body { position: relative; font-family: "Roboto Condensed", Arial, sans-serif; }

  .banner { position: absolute; border: 1px solid var(--frame); background: var(--white); overflow: hidden; }
  .banner__stage { position: absolute; background: linear-gradient(135deg, var(--blue-dark) 0%, var(--blue-mid) 55%, var(--blue-light) 100%); overflow: hidden; }

  .logo { position: absolute; color: var(--logo-blue); font-weight: 400; line-height: 1; white-space: nowrap; }
  .logo__tagline { position: absolute; color: var(--logo-blue); font-weight: 400; line-height: 1; white-space: nowrap; }

  .headline { position: absolute; color: var(--white); font-weight: 700; text-transform: uppercase; line-height: 1; text-shadow: 0 2px 3px rgba(0,0,0,.3); white-space: nowrap; }

  .mattress { position: absolute; border-radius: 6px;
    background: linear-gradient(170deg, var(--mattress-light) 0%, #e6e8eb 55%, var(--mattress-shade) 100%);
    transform: skewX(-12deg); box-shadow: 0 4px 8px rgba(0,0,0,.25); }

  .badge { position: absolute; border-radius: 50%; background: var(--green); border: 6px solid var(--white);
    color: var(--white); font-weight: 700; text-align: center; display: flex; align-items: center; justify-content: center; line-height: 1.15; }

  .benefits { position: absolute; list-style: none; color: var(--green-text); font-weight: 400; line-height: 1.55; white-space: nowrap; }
  .benefits li::before { content: "› "; }

  .cta { position: absolute; background: var(--green); color: var(--white); font-weight: 700; text-transform: uppercase;
    display: flex; align-items: center; justify-content: center; }

  /* Skyscraper 160 x 600 */
  .sky { left: 8px; top: 8px; width: 258px; height: 978px; }
  .sky .banner__stage { left: 0; top: 0; width: 256px; height: 742px; }
  .sky .logo { left: 14px; top: 42px; font-size: 33px; }
  .sky .logo__tagline { left: 14px; top: 88px; font-size: 19px; }
  .sky .headline--main { left: 0; width: 256px; text-align: center; top: 222px; font-size: 60px; line-height: 64px; }
  .sky .headline--sub { left: 0; width: 256px; text-align: center; top: 352px; font-size: 38px; line-height: 48px; }
  .sky .mattress { left: -20px; top: 585px; width: 290px; height: 150px; }
  .sky .badge { left: 72px; top: 480px; width: 136px; height: 136px; font-size: 21px; }
  .sky .benefits { left: 14px; top: 808px; font-size: 16px; }
  .sky .benefits li:nth-child(2) { padding-left: 14px; }
  .sky .cta { left: 22px; top: 866px; width: 216px; height: 68px; font-size: 18px; }

  /* Medium rectangle 300 x 250 */
  .rect { left: 286px; top: 580px; width: 486px; height: 406px; }
  .rect .banner__stage { left: 0; top: 0; width: 484px; height: 327px; }
  .rect .logo { left: 46px; top: 26px; font-size: 33px; }
  .rect .logo__tagline { left: 46px; top: 70px; font-size: 19px; }
  .rect .headline--main { left: 46px; top: 102px; font-size: 50px; }
  .rect .headline--sub { left: 46px; top: 156px; font-size: 23px; }
  .rect .mattress { left: 90px; top: 200px; width: 330px; height: 130px; }
  .rect .badge { left: 296px; top: 186px; width: 136px; height: 136px; font-size: 21px; }
  .rect .benefits { left: 16px; top: 346px; font-size: 16px; }
  .rect .benefits li:nth-child(2) { padding-left: 26px; }
  .rect .cta { left: 278px; top: 338px; width: 180px; height: 56px; font-size: 18px; }

  /* Leaderboard 728 x 90 */
  .leader { left: 8px; top: 1004px; width: 1187px; height: 147px; }
  .leader .banner__stage { left: 0; top: 0; width: 932px; height: 145px; }
  .leader .logo { left: 22px; top: 30px; font-size: 33px; }
  .leader .logo__tagline { left: 22px; top: 96px; font-size: 19px; }
  .leader .headline--main { left: 294px; top: 38px; font-size: 46px; }
  .leader .headline--sub { left: 294px; top: 88px; font-size: 23px; }
  .leader .mattress { left: 630px; top: 20px; width: 260px; height: 110px; }
  .leader .badge { left: 784px; top: 8px; width: 130px; height: 130px; font-size: 20px; }
  .leader .benefits { left: 955px; top: 24px; font-size: 16px; }
  .leader .benefits li:nth-child(2) { padding-left: 16px; }
  .leader .cta { left: 973px; top: 72px; width: 178px; height: 56px; font-size: 18px; }
</style>
</head>
<body>

<section class="banner sky" aria-label="Banner 160 x 600">
  <div class="banner__stage">
    <div class="logo">Schlummerhaus</div>
    <div class="logo__tagline">matratzen online bestellen</div>
    <div class="headline headline--main">Weil Ihr<br>Schlaf</div>
    <div class="headline headline--sub">Den Tag<br>Bestimmt</div>
    <div class="mattress" role="img" aria-label="Foto einer weißen gesteppten Matratze"></div>
    <div class="badge">100 Tage<br>Probe<br>Schlafen!</div>
  </div>
  <ul class="benefits">
    <li>Versandkostenfreier Versand!</li>
    <li>Blauer Anker geprüft!</li>
  </ul>
  <div class="cta">Mehr erfahren</div>
</section>

<section class="banner rect" aria-label="Banner 300 x 250">
  <div class="banner__stage">
    <div class="logo">Schlummerhaus</div>
    <div class="logo__tagline">matratzen online bestellen</div>
    <div class="headline headline--main">Weil Ihr Schlaf</div>
    <div class="headline headline--sub">Den Tag Bestimmt</div>
    <div class="mattress" role="img" aria-label="Foto einer weißen gesteppten Matratze"></div>
    <div class="badge">100 Tage<br>Probe<br>Schlafen!</div>
  </div>
  <ul class="benefits">
    <li>Versandkostenfreier Versand!</li>
    <li>Blauer Anker geprüft!</li>
  </ul>
  <div class="cta">Mehr erfahren</div>
</section>

<section class="banner leader" aria-label="Banner 728 x 90">
  <div class="banner__stage">
    <div class="logo">Schlummerhaus</div>
    <div class="logo__tagline">matratzen online bestellen</div>
    <div class="headline headline--main">Weil Ihr Schlaf</div>
    <div class="headline headline--sub">Den Tag Bestimmt</div>
    <div class="mattress" role="img" aria-label="Foto einer weißen gesteppten Matratze"></div>
    <div class="badge">100 Tage<br>Probe<br>Schlafen!</div>
  </div>
  <ul class="benefits">
    <li>Versandkostenfreier Versand!</li>
    <li>Blauer Anker geprüft!</li>
  </ul>
  <div class="cta">Mehr erfahren</div>
</section>

</body>
</html>
```